DL, Tri Fold Flyer - Keen On Gizmos

We need DL Tri Fold Brochure designed to print and distribute to primary schools in Australia advertising our exciting and educational science workshops.

Fun, exciting yet with a professional/educational edge. Similar to the feel of our website science shop www.keenongizmos.com.au and/or incursion page keenongizmosvisits.com.au

Design should be fresh, clean and simple, eye-catching with a sense of quality.

There needs to be visual interest with graphic elements and pictures to break up the text. To be print ready with bleed and cut lines indicated for printer. Roll fold, 2 -sided, and full colour.

Please see the attached file KeenOnGizmosBrochureDesignBrief2018 for complete text and layout requirements.

I have also attached some previous designs for 2015, 2016, 2017 to give an idea of what is required and what has been designed in the past.

Target Market(s)

Primary school teachers in Australia

Industry/Entity Type

Education

Font styles to use
Sans Serif

Requirements
Must have
• Logo
• Images
• All the information included in the attached file KeenOnGizmosBrochureDesignBrief2018
Nice to have
• Eyecatching graphics and text

```html
<!DOCTYPE html>
<html lang="en">
<head>
<meta charset="utf-8">
<title>Keen On Gizmos – Workshop Topics</title>
<link href="https://fonts.googleapis.com/css2?family=Barlow+Semi+Condensed:ital,wght@0,300;0,400;1,400&family=Barlow:wght@500;600;700&display=swap" rel="stylesheet">
<style>
  :root{
    --page-bg:#d3e4ec;
    --sheet:#ffffff;
    --tab-blue:#0a72b0;
    --head-blue:#0b6fa8;
    --topic-orange:#e65f1b;
    --body-text:#3d3d3d;
    --bubble:#e4f3f4;
    --glass:#8fd0e0;
  }
  *{box-sizing:border-box;margin:0;padding:0}
  html,body{width:1200px;height:1200px;overflow:hidden;background:var(--page-bg)}
  .sheet{
    position:absolute;left:30px;top:196px;width:1140px;height:807px;
    background:var(--sheet);overflow:hidden;
    box-shadow:0 4px 14px rgba(30,60,80,.18);
  }
  .bubbles{position:absolute;inset:0;width:100%;height:100%}
  .bubbles circle{fill:var(--bubble)}
  .tab{
    position:absolute;left:0;top:0;width:290px;height:40px;
    background:var(--tab-blue);
    clip-path:polygon(0 0,100% 0,94% 100%,0 100%);
    color:#fff;font:700 19px/40px "Barlow",sans-serif;letter-spacing:.5px;
    padding-left:35px;
  }
  .column{
    position:absolute;width:356px;
    font-family:"Barlow Semi Condensed",sans-serif;
    font-weight:300;font-size:10.4px;line-height:14.6px;color:var(--body-text);
  }
  .col-1{left:14px;top:55px}
  .col-2{left:392px;top:17px}
  .col-3{left:773px;top:17px}
  .section{
    font-family:"Barlow",sans-serif;font-weight:600;font-size:14px;line-height:18px;
    color:var(--head-blue);margin:10px 0 1px;
  }
  .section:first-child{margin-top:0}
  .topic{
    font-style:italic;font-weight:400;font-size:11px;line-height:15px;
    color:var(--topic-orange);margin-top:5px;
  }
  .section + .topic{margin-top:0}
  .column > .topic:first-child{margin-top:0}
  .topic .plain{font-style:normal;color:#222}
  .glassware{
    position:absolute;left:968px;top:714px;width:130px;height:76px;
    background:linear-gradient(90deg,#f3c6d4 0%,#f6dc6a 40%,var(--glass) 70%);
    border-radius:6px;opacity:.85;
  }
</style>
</head>
<body>
<main class="sheet">
  <svg class="bubbles" viewBox="0 0 1140 807" aria-hidden="true">
    <circle cx="340" cy="138" r="140"/>
    <circle cx="157" cy="352" r="58"/>
    <circle cx="298" cy="493" r="87"/>
    <circle cx="414" cy="489" r="37"/>
    <circle cx="265" cy="717" r="21"/>
    <circle cx="737" cy="96" r="23"/>
    <circle cx="696" cy="313" r="75"/>
    <circle cx="663" cy="692" r="157"/>
    <circle cx="1077" cy="311" r="66"/>
    <circle cx="1102" cy="519" r="37"/>
    <circle cx="1052" cy="100" r="33"/>
  </svg>

  <div class="tab">WORKSHOP TOPICS</div>

  <section class="column col-1">
    <h2 class="section">CHEMICAL SCIENCES</h2>
    <h3 class="topic">Chemistry Chaos - Foundation to Level 6</h3>
    <p>Colour changes, smoke, fizz and foam! Everything in our world is made-up of chemicals: explore interesting polymer chemicals, chemical reactions, reversible physical changes and more. Available in a junior or senior format.</p>
    <h3 class="topic">The Matter Of Matter - Level 3 to 6</h3>
    <p>Use the magic of dry ice to explore the three common states of matter - solids, liquids and gasses. From everlasting bubbling fountains to cool chemical fire extinguishers. This session matters! (90 minute format only) Incurs a $20 per day dry ice surcharge.</p>
    <h3 class="topic">Forensic Detective – Level 3 to 6</h3>
    <p>Can you crack the case and catch the thief!? Use real forensic science techniques, like PH tests, ink chromatography, glow chemicals, and fingerprint dusting to pin point the culprit. (90 minute format only).</p>
    <h3 class="topic">Super Bubble Science – Foundation to Level 2</h3>
    <p>Bubbles are more than trapped air in a film of soapy water. Their exact spherical shape and swirling rainbow colours make them a wonder of science. By this session’s end, you’ll be a true bubbliologist.</p>
    <h3 class="topic">Kitchen Chemistry – Foundation to Level 2</h3>
    <p>A fun food workshop challenging you to think about everyday food in a whole new way. Experiment with a variety of food-related chemicals, and you even get to take home a bag of sweet, tongue tingling sherbet!</p>
    <h3 class="topic">Material Science – Foundation to Level 6</h3>
    <p>Explore the world around you - sort, classify and test the physical properties of natural and processed materials. Discover how materials can change physically as well as chemically. Mix a material concoction for a purpose, explore the effect of heat on materials, material waste and remake a material into a new product.</p>

    <h2 class="section">PHYSICAL SCIENCES</h2>
    <h3 class="topic">Forces In Action – Foundation to 6</h3>
    <p>From an apple falling to the ground to a car rolling to a halt, forces are constantly at work. Explore gyroscopes, flying tops, friction and inertia during this stimulating, hands-on look at how things move, and why! Available in a junior or senior format.</p>
    <h3 class="topic">Light and Sound – Foundation to Level 2</h3>
    <p>Make some waves, and colour your classroom with rainbows. Using a sensory approach learn all about the properties and transmission of light and sound energy.</p>
    <h3 class="topic">Electrical Buzz – Foundation to Level 6</h3>
    <p>Lights, noise and airborne propellers. Use snap circuit kits to build exciting circuits using a variety of electrical components including switches, LEDs, resistors and integrated sound circuits. Explore electric motors, electromagnets, dynamos, and energy transformations. Includes a demonstration of how electricity is produced from sun light.</p>
  </section>

  <section class="column col-2">
    <h3 class="topic">Simple Machines – Level 3 to 6</h3>
    <p>Launch projectiles with D.I.Y catapults, watch motorized gears turn to speed things up, and lift friends off the ground with a super-sized lever. An engaging look at how simple machines make our life easier, now, and in the past. (90 minute format only)</p>
    <h3 class="topic">Light &amp; Colour – Foundation to Level 2</h3>
    <p>An engaging investigation into the colourful properties of light. Create rainbows, use chromatography to separate colour in ink, mix colour with light filters and test a whole host of optical instruments.</p>
    <h3 class="topic">Toy Technology – Foundation to Level 2</h3>
    <p>Be immersed in the wonderful science of toys. Explore energies, materials, movement and sound. Spin some colour, use magnets to draw, and even make your very own balancing toy to take home. Play has never been so educational!</p>
    <h3 class="topic">Light Senior – Level 3 to 6</h3>
    <p>This senior primary workshop takes an in-depth look at the properties of light - within and outside the visible spectrum. Get hands-on with a variety of interesting optical instruments, explore UV light and make a UV detection key chain to keep, watch light energy transform, discover different ways to produce light, including chemiluminescence, and more!</p>

    <h2 class="section">BIOLOGICAL SCIENCES</h2>
    <h3 class="topic">Living Things – Foundation to Level 6</h3>
    <p>This workshop is full of life. Explore objects that have self-sustaining processes like plants, animals and mirco-organisms. Through engaging hands-on activities learn about the difference between living and non-living things, simple life cycles and the bigger picture. Available in a junior or senior format.</p>
    <h3 class="topic">Living Things – Foundation to Level 6</h3>
    <p>This workshop is full of life. Explore objects that have self-sustaining processes like plants, animals and mirco-organisms. Through engaging hands-on activities learn about the difference between living and non-living things, simple life cycles and the bigger picture. Available in a junior or senior format.</p>
    <h3 class="topic">Senses – Foundation to Level 2</h3>
    <p>The five senses are given a workout in this engaging session. They are tested, tricked and more.</p>
    <h3 class="topic">The Human Body – Level 3 to 6</h3>
    <p>Take a journey through the human body, and explore its parts and systems. Perform chemical experiments to understand digestion, think quick and test reaction speeds, use stethoscopes to listen to the rhythmic beat of your heart. Learn how we are all connected, and made of the stuff of stars!</p>

    <h2 class="section">EARTH &amp; SPACE SCIENCES</h2>
    <h3 class="topic">Wicked Weather – Foundation to Level 2</h3>
    <p>Air in the atmosphere is always on the move, carrying clouds, rain, and snow around the globe. Model and experiment with these air and water movements; and even erupt your own flurry of snow.</p>
  </section>

  <section class="column col-3">
    <h3 class="topic">Natural Disasters – Level 3 to 6</h3>
    <p>Explore the scientific processes behind the explosive energy of nature’s fury.</p>
    <h3 class="topic">Global Sustainability – Level 1 to 6</h3>
    <p>The phenomenal population boom in recent times has put the earth’s resources under considerable strain. Learn how we can better manage waste and the earth’s life sustaining resources to build a better future for all.</p>
    <h3 class="topic">Earth &amp; The Milky Way – Level 3 to 6</h3>
    <p>Space is a vacuum but it is far from empty. During this fascinating workshop you’ll launch into space and explore planets, moons, stars and galaxies. Follow in the footsteps of the great astronomers as you probe the mystery, scale and earth’s place in the universe.</p>
    <h3 class="topic">Rocks &amp; Geology – Level 3 to 6</h3>
    <p>It is written in the rocks. Read the changing story of earth and the impact of humans through the pages of rocks. Cast your own fossil, explore and classify rocks and minerals, investigate the characteristics of soil, model the layers of earth, create some explosive lava flows. Everything to enthuse young geologists!</p>
    <h3 class="topic">Water &amp; The Environment <span class="plain">– Foundation to Level 4</span></h3>
    <p>Water is essential to life, and is our most precious resource. We use it to drink, for cooking,washing and hygiene, recreation, industry and agriculture. During this workshop students develop an understanding and appreciation of the importance and special properties of water.</p>

    <h2 class="section">Science, Technology, Engineering &amp; Mathematics</h2>
    <h3 class="topic">Buzzbot Robotics – Foundation to Level 2</h3>
    <p>An introduction to robots and programming for younger students. With an intuitive interface, colourful buzzbot will have learners excited about simple sequencing and directional language. Equipment surcharge applies.</p>
    <h3 class="topic">qBot Robotics Programming – Level 3 to 6</h3>
    <p>Meet friendly qBOT, a STEM educational robot to learn coding and robotics. Drag-and-drop graphical programming makes learning Circuino easy and crazy-fun! Available in a 90 minute format only at $380 plus GST per session.</p>
    <h3 class="topic">Circuit Board Electronics – Level 5 &amp; 6</h3>
    <p>Solder electronic components onto specially-designed circuit boards. Take home your own working electronic device like an alarm, lie detector or game. Maximum 20 students. Available in a 90 minute format only at $480 plus GST per session.</p>
    <h3 class="topic">3D Drawing – Level 1 to 6</h3>
    <p>This STEM workshop has you inventing and creating in 3D. Using 3D pen technology, design your own plastic model for a purpose.</p>
    <h3 class="topic">GIZMO SCIENCE SHOW – Foundation to Level 6</h3>
    <p>A jam-packed 60 min show of BIG WOW! science madness! There’s giant smoke vortices, levitating beach balls, flying toilet paper, flour fire-balls, hair-raising electricity, and lots of learning! Suitable for up to 180 students. Price $650 plus GST</p>
  </section>

  <div class="glassware" role="img" aria-label="Illustration of two test tubes with pink and yellow liquid beside a blue conical lab flask"></div>
</main>
</body>
</html>
```